Podcast cover art (not a logo)

I’m launching an audio-only podcast for parents of neurodivergent children. The podcast is meant to feel like a calm, trusted professional voice — not a brand or a performance.

Style direction:
--Clean and minimal
--Calm and grounded
--Professional, not playful
--Nothing flashy, loud, or busy
--No cartoon imagery

Content on the cover:
--Podcast title: Rooted in Listening
--Subtitle or tagline: Supporting Neurodivergent Kids with Science, Not Shame (or Understanding Neurodivergent Kids)
--No episode numbers, no dates

Design preferences:
--Text-forward design
--Neutral or soft colors (muted blues, grays, off-whites)
--High contrast for readability at small sizes
--Simple, timeless font

What I do NOT want:
--A logo or branding system
--Illustrations of children or families
--Bright colors or playful graphics
--Trendy fonts or visual effects

Technical requirements:
--Square image
--3000 × 3000 pixels
--RGB color mode
--JPEG or PNG
--File size under 500 KB

Deliverables:
--Final cover art file
--Optional: one or two alternate background color versions

```html
<!DOCTYPE html>
<html lang="en">
<head>
<meta charset="utf-8">
<title>Rooted in Listening — Podcast Cover</title>
<link href="https://fonts.googleapis.com/css2?family=Montserrat:wght@500;600&display=swap" rel="stylesheet">
<style>
  :root {
    --page-bg: #e6e8ea;
    --cover-center: #eef4f9;
    --cover-mid: #c6dcea;
    --cover-edge: #a0c5dd;
    --swoosh: #8db6d4;
    --swoosh-edge: #b3d0e4;
    --title: #4b7d86;
    --subtitle: #0d0d0d;
    --brain-tone: #7fb0c9;
    --mic: #d9e8f2;
  }
  * { margin: 0; padding: 0; box-sizing: border-box; }
  html, body {
    width: 1018px;
    height: 1200px;
    overflow: hidden;
    background: var(--page-bg);
  }
  .canvas {
    position: relative;
    width: 1018px;
    height: 1200px;
  }
  .cover {
    position: absolute;
    left: 39px;
    top: 130px;
    width: 940px;
    height: 940px;
    overflow: hidden;
    background: radial-gradient(circle at 50% 44%, var(--cover-center) 0%, var(--cover-mid) 38%, var(--cover-edge) 80%);
    box-shadow: 0 8px 24px rgba(0, 0, 0, 0.12);
  }
  .cover__swoosh {
    position: absolute;
    inset: 0;
    width: 940px;
    height: 940px;
  }
  .cover__artwork {
    position: absolute;
    left: 298px;
    top: 224px;
    width: 320px;
    height: 221px;
    border-radius: 48% 52% 46% 50% / 58% 56% 44% 42%;
    background: radial-gradient(ellipse at 50% 50%, rgba(127, 176, 201, 0.35), rgba(127, 176, 201, 0.12) 70%, rgba(127, 176, 201, 0) 100%);
  }
  .cover__text {
    position: absolute;
    left: 0;
    right: 0;
    top: 460px;
    text-align: center;
    font-family: "Montserrat", sans-serif;
  }
  .cover__title {
    font-weight: 600;
    font-size: 54px;
    letter-spacing: 1px;
    color: var(--title);
    line-height: 1.1;
  }
  .cover__subtitle {
    margin-top: 14px;
    font-weight: 600;
    font-size: 33px;
    line-height: 41px;
    color: var(--subtitle);
    letter-spacing: 0.5px;
  }
  .cover__mic {
    position: absolute;
    left: 829px;
    top: 787px;
    width: 64px;
    height: 110px;
  }
</style>
</head>
<body>
<main class="canvas">
  <section class="cover">
    <svg class="cover__swoosh" viewBox="0 0 940 940" aria-hidden="true">
      <path d="M490 940 C700 890 900 780 940 640 L940 940 Z" fill="var(--swoosh)"/>
      <path d="M490 940 C700 890 900 780 940 640" fill="none" stroke="var(--swoosh-edge)" stroke-width="4"/>
    </svg>

    <div class="cover__artwork" role="img" aria-label="Line drawing of a brain made of interlocking puzzle pieces"></div>

    <div class="cover__text">
      <h1 class="cover__title">Rooted in Listening</h1>
      <p class="cover__subtitle">Supporting Neurodivergent Kids<br>with Science, Not Shame</p>
    </div>

    <svg class="cover__mic" viewBox="0 0 64 110" aria-hidden="true">
      <g fill="none" stroke="var(--mic)" stroke-width="5" stroke-linecap="round">
        <rect x="16" y="3" width="32" height="62" rx="16"/>
        <path d="M4 40 V52 A28 28 0 0 0 60 52 V40"/>
        <line x1="32" y1="80" x2="32" y2="102"/>
        <line x1="20" y1="105" x2="44" y2="105"/>
        <line x1="16" y1="20" x2="24" y2="20"/>
        <line x1="40" y1="20" x2="48" y2="20"/>
        <line x1="16" y1="30" x2="24" y2="30"/>
        <line x1="40" y1="30" x2="48" y2="30"/>
        <line x1="16" y1="40" x2="24" y2="40"/>
        <line x1="40" y1="40" x2="48" y2="40"/>
        <line x1="16" y1="50" x2="24" y2="50"/>
        <line x1="40" y1="50" x2="48" y2="50"/>
      </g>
    </svg>
  </section>
</main>
</body>
</html>
```